Business Card Design

Buy and sell properties
Buy and rehab properties
Buy properties for cash
That is what I do but do need a logo
looking for some type of logo or design on it
Just started business
Back of card should say something like BUY HOUSES CASH
Overview: it is a new company. Basically I buy properties wholesale and fix them up and sell them or sell them to other fix and flippers
Background: company is new so not any background
Market: is basically anyone selling a house or buying a house. Someone that needs to sell house fast. Basically I am a cash home buyer!!!

Email on card should be:   harborvalepropertiesinc@example-mail.com

Industry/Entity Type
House
Contact Information for Business Card
Harbor Vale Properties Inc
PO Box 718264
Coral Marsh FL 34197

Dale Morcott
dmorcott@example-mail.com
555-271-9083

```html
<!DOCTYPE html>
<html lang="en">
<head>
<meta charset="utf-8">
<title>Harbor Vale Properties Inc – Business Card</title>
<link href="https://fonts.googleapis.com/css2?family=Arimo:wght@400;700&display=swap" rel="stylesheet">
<style>
  :root {
    --page: #ffffff;
    --frame: #cfcfcf;
    --card-dark: #000000;
    --card-light: #ffffff;
    --card-edge: #9a9a9a;
    --ink-light: #ffffff;
    --ink-brand: #333333;
    --ink-text: #5a5a5a;
    --rule: #8a8a8a;
    --mark-dark: #bdbdbd;
    --mark-light: #6e6e6e;
  }
  * { margin: 0; padding: 0; box-sizing: border-box; }
  html, body { width: 1200px; height: 1000px; overflow: hidden; background: var(--page); }
  body { font-family: "Arimo", Arial, sans-serif; position: relative; }
  .canvas {
    position: absolute; inset: 0;
    border: 1px solid var(--frame);
  }
  .card { position: absolute; width: 488px; height: 279px; }
  .card-front {
    left: 359px; top: 181px;
    background: var(--card-dark);
  }
  .front-mark {
    position: absolute; left: 214px; top: 86px;
    width: 60px; height: 60px; border-radius: 50%;
    background: var(--mark-dark);
  }
  .front-brand {
    position: absolute; left: 0; right: 0; top: 166px;
    text-align: center;
    color: var(--ink-light);
    font-weight: 700; font-size: 27px; letter-spacing: 0.2px;
  }
  .card-back {
    left: 355px; top: 547px;
    background: var(--card-light);
    border: 1px solid var(--card-edge);
  }
  .back-mark {
    position: absolute; left: 78px; top: 104px;
    width: 44px; height: 44px; border-radius: 50%;
    background: var(--mark-light);
  }
  .back-brand {
    position: absolute; left: 14px; width: 172px; top: 163px;
    text-align: center;
    color: var(--ink-brand);
    font-weight: 700; font-size: 13px;
  }
  .divider { position: absolute; left: 195px; top: 46px; }
  .holder-name {
    position: absolute; left: 226px; top: 72px;
    color: var(--ink-text);
    font-weight: 700; font-size: 32px; letter-spacing: 0.5px;
  }
  .contact-list {
    position: absolute; left: 226px; top: 130px;
    list-style: none;
    color: var(--ink-text);
    font-weight: 700; font-size: 15px; letter-spacing: 1.2px;
    line-height: 23px;
  }
  .contact-list .email { letter-spacing: 0.6px; }
</style>
</head>
<body>
<main class="canvas">
  <section class="card card-front">
    <span class="front-mark" aria-hidden="true"></span>
    <p class="front-brand">Harbor Vale Properties Inc</p>
  </section>

  <section class="card card-back">
    <span class="back-mark" aria-hidden="true"></span>
    <p class="back-brand">Harbor Vale Properties Inc</p>
    <svg class="divider" width="4" height="194" viewBox="0 0 4 194" aria-hidden="true">
      <path d="M2 0 L3.5 97 L2 194 L0.5 97 Z" fill="var(--rule)"/>
    </svg>
    <h1 class="holder-name">Dale Morcott</h1>
    <ul class="contact-list">
      <li class="phone">555-271-9083</li>
      <li class="address">PO Box 718264</li>
      <li class="address">Coral Marsh FL 34197</li>
      <li class="email">dmorcott@example-mail.com</li>
    </ul>
  </section>
</main>
</body>
</html>
```